We need a design for our retail display and for our stockist's retail display.
Our product is fresh corn tortillas. These can be used to make tacos, quesadillas, tortilla chips and tostadas.
We want the table talker to use our brand style (see our website) and show the tortillas versatility.
kelvo-flatbreads.co.uk
It should also have a space for our stockists to write in a blank space under the heading "Our fresh tortillas are delivered every....[blank space]"
The table talker should be 75mm tall x 150mm wide. This will also have a 25mm self adhesive flap at the top which can be blank or the same colour as the background.
Please feel free to use any files from our website as well as illustrations attached.
Target Market(s)
Customers in high end shops and delis
Industry/Entity Type
food and drink
Look and feel

```html
<!DOCTYPE html>
<html lang="en">
<head>
<meta charset="utf-8">
<title>Kelvo Flatbreads – Table Talker</title>
<link href="https://fonts.googleapis.com/css2?family=Montserrat:wght@400;500;700&display=swap" rel="stylesheet">
<style>
  :root {
    --backdrop: #dcdde1;
    --paper: #ffffff;
    --navy: #1e2d45;
    --gold: #e3c022;
    --mist: #c3c4c9;
    --corn-light: #e6d6bc;
    --corn-mid: #c9b08a;
    --corn-dark: #9d8564;
  }
  * { box-sizing: border-box; margin: 0; padding: 0; }
  html, body { width: 1200px; height: 965px; overflow: hidden; }
  body {
    background: var(--backdrop);
    font-family: "Montserrat", Arial, sans-serif;
    position: relative;
  }
  .table-talker {
    position: absolute;
    left: 60px; top: 122px;
    width: 1080px; height: 720px;
    background: var(--paper);
    overflow: hidden;
    box-shadow: 0 6px 16px rgba(0,0,0,0.18);
  }
  .adhesive-flap {
    position: absolute; left: 0; top: 0;
    width: 100%; height: 180px;
    background: var(--paper);
  }
  .headline-band {
    position: absolute; left: 0; top: 180px;
    width: 100%; height: 70px;
    background: var(--navy);
  }
  .headline {
    position: absolute; left: 300px; top: 198px;
    color: var(--gold);
    font-weight: 700;
    font-size: 27px;
    letter-spacing: 1.2px;
    white-space: nowrap;
  }
  .product-photo {
    position: absolute; left: 0; top: 240px;
    width: 100%; height: 230px;
    background: linear-gradient(180deg, var(--corn-light) 0%, var(--corn-mid) 55%, var(--corn-dark) 100%);
  }
  .band-edge { position: absolute; left: 0; width: 100%; display: block; }
  .logo-panel {
    position: absolute; left: 24px; top: 176px;
    width: 240px; height: 280px;
    background: var(--mist);
    opacity: 0.85;
  }
  .logo-badge {
    position: absolute; left: 44px; top: 192px;
    width: 200px; height: 200px;
    border-radius: 50%;
    background: var(--navy);
    display: flex; flex-direction: column;
    align-items: center; justify-content: center;
    color: var(--gold);
    font-weight: 700;
    text-align: center;
    line-height: 1.15;
  }
  .logo-badge .brand-main { font-size: 40px; }
  .logo-badge .brand-sub { font-size: 15px; letter-spacing: 3px; }
  .uses-bar {
    position: absolute; left: 40px; top: 475px;
    width: 1000px; height: 40px;
    background: var(--navy);
    border-radius: 20px;
    display: flex;
  }
  .use-label {
    flex: 1;
    display: flex; align-items: center; justify-content: center;
    color: var(--gold);
    font-weight: 700;
    font-size: 20px;
    letter-spacing: 0.5px;
  }
  .use-label + .use-label {
    border-left: 3px solid var(--paper);
  }
  .uses-illustrations {
    position: absolute; left: 40px; top: 525px;
    width: 1000px; height: 80px;
    display: flex;
  }
  .dish-slot { flex: 1; display: flex; justify-content: center; align-items: center; }
  .dish-illustration {
    width: 78px; height: 66px;
    border-radius: 12px;
    background: linear-gradient(135deg, #f1f1f1, #bdbdbd);
  }
  .delivery-band {
    position: absolute; left: 0; top: 612px;
    width: 100%; height: 108px;
    background: var(--gold);
  }
  .delivery-note {
    position: absolute; left: 270px; top: 640px;
    color: var(--navy);
    font-weight: 400;
    font-size: 26px;
    letter-spacing: 1px;
    white-space: nowrap;
  }
</style>
</head>
<body>
  <main class="table-talker">
    <div class="adhesive-flap"></div>

    <div class="product-photo" role="img" aria-label="Photograph of tall stacks of fresh corn tortillas"></div>

    <div class="headline-band"></div>
    <svg class="band-edge" style="top:240px" width="1080" height="18" viewBox="0 0 1080 18" aria-hidden="true">
      <path d="M0 0 H1080 V6 Q1010 14 940 8 T800 10 T660 7 T520 11 T380 8 T240 12 T100 9 T0 12 Z" fill="#1e2d45"/>
      <path d="M0 12 Q50 6 100 9 T240 12 T380 8 T520 11 T660 7 T800 10 T940 8 T1080 6" fill="none" stroke="#ffffff" stroke-width="2.5"/>
    </svg>
    <p class="headline">EXPLORE THE POSSIBILITES WITH OUR TORTILLAS</p>

    <div class="logo-panel"></div>
    <div class="logo-badge" aria-label="Kelvo Flatbreads">
      <span class="brand-main">Kelvo</span>
      <span class="brand-sub">FLATBREADS</span>
    </div>

    <svg class="band-edge" style="top:450px" width="1080" height="30" viewBox="0 0 1080 30" aria-hidden="true">
      <path d="M0 30 V18 L80 20 L160 14 L250 19 L340 12 L420 17 L520 10 L600 15 L700 8 L780 13 L880 6 L960 11 L1080 4 V30 Z" fill="#ffffff"/>
    </svg>

    <nav class="uses-bar" aria-label="Tortilla uses">
      <span class="use-label">QUESADILLAS</span>
      <span class="use-label">TACOS</span>
      <span class="use-label">TORTILLA CHIPS</span>
      <span class="use-label">TAQUITOS</span>
      <span class="use-label">TOSTADAS</span>
    </nav>

    <div class="uses-illustrations">
      <div class="dish-slot"><div class="dish-illustration" role="img" aria-label="Line drawing of a quesadilla"></div></div>
      <div class="dish-slot"><div class="dish-illustration" role="img" aria-label="Line drawing of a taco"></div></div>
      <div class="dish-slot"><div class="dish-illustration" role="img" aria-label="Line drawing of a tortilla chip with dip"></div></div>
      <div class="dish-slot"><div class="dish-illustration" role="img" aria-label="Line drawing of a taquito"></div></div>
      <div class="dish-slot"><div class="dish-illustration" role="img" aria-label="Line drawing of a topped tostada"></div></div>
    </div>

    <div class="delivery-band"></div>
    <svg class="band-edge" style="top:596px" width="1080" height="18" viewBox="0 0 1080 18" aria-hidden="true">
      <path d="M0 18 V12 L90 14 L170 9 L260 13 L350 7 L440 11 L540 6 L630 10 L730 4 L820 8 L920 3 L1000 7 L1080 2 V18 Z" fill="#e3c022"/>
    </svg>
    <p class="delivery-note">Our fresh tortillas are delivered every</p>
  </main>
</body>
</html>
```